Design new Brackwater Asset business card 2016

We need a new business card for our company Brackwater Asset Partners. We are a niche Alternative Investment Fund Manager based in Chester, in the North West of the UK.We market our services to global institutions such as banks, insurance companies, pension funds, etc. as well as wealthy individuals. Our main markets are Europe (Germany\France\Switzerland), the US and parts of Asia.
The design needs to be in line with existing company branding. Life the assets we deal with, the business card might suggest, "niche\alternative" type of attributes - however, it needs to remain professional, clean and appropriate for our client base.
Our existing business card format with relevant factual information is included, along with logo and branding details.

Target Market(s)

We market our services to global institutions such as banks, insurance companies, pension funds, etc. as well as wealthy individuals.

Industry/Entity Type

Financial Service

Contact Information for Business Card

please see attached pdf for information on existing business card which we should aim to convey on your new design. However:
- the wording "Brackwater Asset Partners Ltd is Authorised and Regulated
by the Monetary Oversight Bureau. Registered No. 7139046" should be replaced with , "Brackwater Asset Partners Ltd is an Alternative Investment Fund Manager Authorised and Regulated by the Monetary Oversight Bureau. Registered No. 7139046"
- the "reception" word on reverse can be omitted.
- the "retail: www.toplivanex.co.uk" wording can be omitted.
- the QR code is not required in the new version.

Font styles to use
Serif
Sans Serif

Requirements
Must have
• information on current business card, subject to comments provided above.
Nice to have
• Use of areas of solid colour instead of large areas of white space might be nice to experiment with. However, still need to have the general look and feel of the brand as presented on our website www.bwfundco.co.uk
• If we had space for 3 bullet points describing what we do\who we are, this might be good to try out. e.g. alternative investment fund manager, longevity specialist, founded 1990.
• Also, we have a new tag line, "expertise with longevity" which might fit nicely somewhere on the business card.
Should not have
• - no QR code
• - should not use all the colours in our logo as it looks very garish! Using one or two colours with black\white etc, seems to work better.

```html
<!DOCTYPE html>
<html lang="en">
<head>
<meta charset="utf-8">
<title>Brackwater Asset Partners – Business Card</title>
<link rel="stylesheet" href="https://fonts.googleapis.com/css2?family=Source+Sans+3:wght@400;600;700&display=swap">
<style>
  :root {
    --stage: #000000;
    --card: #ffffff;
    --brown: #5a2a12;
    --olive: #9a9413;
    --rule: #d9d6cc;
    --accent-soft: #c9b98a;
  }
  * { margin: 0; padding: 0; box-sizing: border-box; }
  html, body { width: 1200px; height: 900px; overflow: hidden; background: var(--stage); }
  body { position: relative; font-family: "Source Sans 3", "Myriad Pro", Arial, sans-serif; color: var(--brown); }

  .card {
    position: absolute;
    top: 271px;
    width: 457px;
    height: 281px;
    background: var(--card);
    border-radius: 14px;
    overflow: hidden;
  }
  .card--front { left: 137px; }
  .card--back { left: 626px; }

  /* Front */
  .brand-mark {
    position: absolute;
    left: 58px; top: 62px;
    width: 84px; height: 84px;
    border-radius: 50%;
    background: var(--accent-soft);
  }
  .brand-name {
    position: absolute;
    font-weight: 600;
    color: var(--brown);
    line-height: 1.1;
  }
  .card--front .brand-name { left: 28px; top: 160px; width: 210px; text-align: center; font-size: 21px; }
  .divider {
    position: absolute; left: 257px; top: 72px;
    width: 1px; height: 144px; background: var(--rule);
  }
  .person { position: absolute; left: 273px; top: 74px; }
  .person__name { font-size: 16.5px; font-weight: 700; color: var(--olive); line-height: 1.1; }
  .person__role { font-size: 12.5px; color: var(--brown); margin-top: 2px; }
  .contacts { position: absolute; left: 273px; top: 129px; list-style: none; }
  .contacts li { display: flex; align-items: center; height: 19px; font-size: 12.5px; }
  .contacts svg { width: 10px; height: 10px; margin-right: 7px; fill: var(--olive); flex: none; }
  .tagline-row {
    position: absolute; left: 0; right: 0; top: 238px;
    display: flex; align-items: center; gap: 8px;
  }
  .tagline-row::before, .tagline-row::after { content: ""; flex: 1; height: 1px; background: var(--olive); }
  .tagline-row::before { flex: 0 0 140px; }
  .tagline { font-size: 14px; font-weight: 600; color: var(--brown); }

  /* Back */
  .card--back .brand-name { left: 22px; top: 36px; font-size: 26px; }
  .statement {
    position: absolute; left: 25px; top: 101px; width: 380px;
    font-size: 12.2px; font-weight: 700; text-transform: uppercase;
    line-height: 19.5px; letter-spacing: 0.1px;
  }
  .highlights { position: absolute; left: 25px; top: 197px; list-style: none; }
  .highlights li { font-size: 12.5px; font-weight: 600; height: 19px; display: flex; align-items: center; }
  .highlights li::before {
    content: ""; width: 6px; height: 6px; border-radius: 50%;
    background: var(--olive); margin-right: 5px;
  }
  .corner-decoration {
    position: absolute; left: 304px; top: 150px;
    width: 160px; height: 160px; border-radius: 50%;
    background: radial-gradient(circle, #e8c77a 0%, #c9b98a 60%, #b39a6a 100%);
  }
</style>
</head>
<body>
  <section class="card card--front">
    <div class="brand-mark"></div>
    <div class="brand-name">Brackwater<br>Asset Partners</div>
    <div class="divider"></div>
    <div class="person">
      <div class="person__name">Martin Hale</div>
      <div class="person__role">Non-Executive Chairman</div>
    </div>
    <ul class="contacts">
      <li><svg viewBox="0 0 10 10"><path d="M2 0.5 L3.6 2.6 L2.7 3.6 C3.3 5 4.8 6.6 6.3 7.3 L7.4 6.4 L9.5 8 L8.4 9.5 C4.5 9 1 5.5 0.5 1.6 Z"/></svg>+44 (0)1632 960418</li>
      <li><svg viewBox="0 0 10 10"><path d="M2.5 0 H7.5 V10 H2.5 Z M3.4 1 V8 H6.6 V1 Z"/></svg>+44 (0)7700 900625</li>
      <li><svg viewBox="0 0 10 10"><path d="M0.5 2 H9.5 V8 H0.5 Z M1 2.4 L5 5.4 L9 2.4" stroke="#fff" stroke-width="0.8"/></svg>mhale@bwfundco.co.uk</li>
      <li><svg viewBox="0 0 10 10"><circle cx="5" cy="5" r="4.8"/><path d="M5 0.5 V9.5 M0.5 5 H9.5" stroke="#fff" stroke-width="0.7"/></svg>www.bwfundco.co.uk</li>
    </ul>
    <div class="tagline-row"><span class="tagline">Expertise with Longevity</span></div>
  </section>

  <section class="card card--back">
    <div class="brand-name">Brackwater Asset Partners</div>
    <p class="statement">Brackwater Asset Partners Ltd is an<br>alternative investment fund manager authorised<br>and regulated by the Monetary Oversight<br>Bureau. Registered No. 7139046.</p>
    <ul class="highlights">
      <li>Alternative investment fund manager</li>
      <li>Longevity specialist</li>
      <li>Founded 1990.</li>
    </ul>
    <div class="corner-decoration" role="img" aria-label="Decorative brand circle"></div>
  </section>
</body>
</html>
```